Health care product retail website

We need a website design for a company based in New Zealand that sells fresh air to an overseas market.
There are 4 products to start with and we have a logo. We need to give the message that it is unpolluted and clean. We are also promoting a self-sustaining business model by investing in the planet's future. The website will be developed in WordPress and if you can suggest coding thats a bonus, but not necessary as I can develop in Wordpress.

Target Market(s)

Chinese, Indian, Middle Eastern or anywhere where the air is quite polluted. middle-income target market

Industry/Entity Type

Health And Wellness

Number of Pages Required

5+ page

Font styles to use
Sans Serif

Requirements
Must have
• Homepage: Clean, fresh look. Indicate that the product is sourced and bottled in a clean environment.
• Any help with e-commerce and multilingual pages appreciated.
• Home, Products, Our locations, Environmental protection, Science

```html
<!DOCTYPE html>
<html lang="en">
<head>
<meta charset="utf-8">
<title>Clearpeak Air – Home</title>
<link href="https://fonts.googleapis.com/css2?family=Roboto:wght@400;500;700&display=swap" rel="stylesheet">
<style>
:root{
  --green:#8dbb1c;
  --green-dark:#7aa514;
  --blue:#0f8fd8;
  --ink:#2e2e2e;
  --muted:#7b7b7b;
  --line:#dcdcdc;
  --panel:#efefef;
  --white:#ffffff;
}
*{margin:0;padding:0;box-sizing:border-box}
html,body{width:716px;height:1200px;overflow:hidden;background:var(--white)}
body{position:relative;font-family:'Roboto',Arial,sans-serif;color:var(--ink)}
.abs{position:absolute}
svg{display:block}

/* header */
.brand{left:95px;top:22px;display:flex;align-items:center;gap:6px}
.brand-mark{width:12px;height:12px;border-radius:50%;background:var(--green)}
.brand-name{font-size:24px;font-weight:700;color:var(--green);letter-spacing:-.3px;white-space:nowrap}
.util-links{top:9px;left:348px;display:flex;gap:15px;font-size:6px;color:#666}
.util-links span{display:flex;align-items:center;gap:3px}
.search{left:350px;top:26px;width:210px;height:20px;border:1px solid #bdbdbd;display:flex;align-items:center;padding-left:7px;gap:6px;font-size:5.5px;color:#888}
.cart{left:573px;top:28px;display:flex;gap:6px;align-items:flex-start}
.cart-badge{position:absolute;left:9px;top:-2px;width:8px;height:8px;border-radius:50%;background:var(--green);color:#fff;font-size:5px;text-align:center;line-height:8px}
.cart-text{font-size:6px;line-height:7.5px;color:#444}
.cart-text b{font-weight:400;color:var(--green);display:block}
.main-nav{top:53px;left:349px;display:flex;align-items:center;font-size:7px;color:#333;height:14px}
.main-nav a{color:inherit;text-decoration:none}
.main-nav .active{background:var(--green);color:#fff;padding:0 9px;height:14px;line-height:14px;margin-right:13px}
.main-nav a+a{margin-right:18px}

/* hero */
.hero{left:0;top:73px;width:716px;height:249px;overflow:hidden}
.hero-photo{width:100%;height:100%;background:radial-gradient(ellipse at 55% 40%,#c9dcc0 0%,#8ea36a 25%,#4e5a33 55%,#2c2f1e 100%)}
.hero-title{left:101px;top:177px;font-size:26px;font-weight:500;color:var(--green)}
.hero-sub{left:101px;top:211px;font-size:9.5px;line-height:13px;color:#fff;width:200px}
.dots{left:338px;top:297px;display:flex;gap:9px}
.dots i{width:6px;height:6px;border-radius:50%;background:#fff}
.dots i.on{background:transparent;border:1px solid #fff}

/* welcome */
.welcome{left:0;top:336px;width:716px;text-align:center}
.welcome h1{font-size:11px;font-weight:700;color:var(--green);letter-spacing:.2px}
.welcome p{margin:8px auto 0;width:420px;font-size:6px;line-height:10.5px;color:var(--muted)}
.btn-green{display:inline-block;background:var(--green);color:#fff;font-size:5.8px;font-weight:700;padding:0 8px;height:15px;line-height:15px;margin-top:9px}

/* products */
.band{left:0;top:432px;width:716px;height:228px;background:var(--panel)}
.tabs{left:95px;top:447px;display:flex;gap:17px;font-size:7.5px;font-weight:500;color:#444}
.tabs .on{color:var(--green);border-bottom:1px solid var(--green);padding-bottom:1px}
.section-title{left:95px;font-size:7.5px;font-weight:500;color:var(--green);border-bottom:1px solid var(--green);padding-bottom:1px}
.pager{left:602px;display:flex;gap:5px}
.grid{left:95px;display:flex;gap:7.7px}
.card{width:126px;height:173px;background:#fff;border:1px solid #e4e4e4;position:relative;text-align:center}
.card .wish{position:absolute;right:8px;top:8px}
.card .shot{width:44px;height:90px;margin:12px auto 0;border-radius:8px}
.shot.white{background:linear-gradient(90deg,#d7d7d7,#fafafa 45%,#cfcfcf)}
.shot.silver{background:linear-gradient(90deg,#bdbdbd,#f3f3f3 45%,#c3c3c3)}
.shot.red{background:linear-gradient(90deg,#a4161a,#e53a33 45%,#9c1418)}
.shot.blue{background:linear-gradient(90deg,#16408f,#3d79cf 45%,#153a84)}
.card .name{margin-top:10px;font-size:7.8px;color:#222}
.card .price{margin-top:2px;font-size:8.6px;font-weight:700;color:var(--green)}
.btn-cart{margin:6px auto 0;width:80px;height:14px;background:var(--blue);color:#fff;font-size:5.4px;font-weight:700;display:flex;align-items:center;justify-content:center;gap:5px}

/* features */
.features{left:95px;top:886px;display:flex;gap:8px}
.feature{width:170px;height:77px;background:var(--green);color:#fff;text-align:center;padding-top:9px}
.feature svg{margin:0 auto}
.feature h3{font-size:8.5px;font-weight:700;margin-top:5px}
.feature p{font-size:5.8px;line-height:9px;margin-top:3px;font-weight:500}

/* newsletter */
.newsletter{left:95px;top:976px;width:525px;height:82px;background:var(--panel);text-align:center}
.newsletter h2{margin-top:15px;display:inline-block;font-size:9.5px;font-weight:500;color:var(--green);border-bottom:1px solid var(--green);padding-bottom:1px}
.field{position:absolute;top:43px;height:24px;background:#fff;border:1px solid #dedede;font-size:5.8px;color:#999;display:flex;align-items:center;gap:5px;padding-left:9px}
.signup{position:absolute;left:372px;top:43px;width:63px;height:24px;background:var(--green);color:#fff;font-size:6.5px;font-weight:700;line-height:24px}

/* footer */
.footer{left:0;top:1082px;width:716px;height:118px;background:var(--panel)}
.footer-brand{left:108px;top:1114px;display:flex;align-items:center;gap:4px}
.footer-brand .brand-name{font-size:13px;letter-spacing:-.2px}
.footer-brand .brand-mark{width:7px;height:7px}
.copyright{left:95px;top:1153px;font-size:5px;color:#555}
.fcol{top:1100px;font-size:5.8px;color:#555;line-height:11.6px}
.fcol h4{font-size:5.8px;font-weight:700;color:#222;margin-bottom:4px}
.fcol .social{display:flex;align-items:center;gap:6px;line-height:14px}
.fcol .social i{width:5px;height:5px;border-radius:50%;background:#555}
</style>
</head>
<body>

<!-- header -->
<div class="abs brand"><span class="brand-mark"></span><span class="brand-name">Clearpeak Air</span></div>

<div class="abs util-links">
  <span><svg width="6" height="6" viewBox="0 0 10 10"><path d="M2 1l2 0 1 2-1.2 1a5 5 0 002.2 2.2L7 5l2 1v2a1 1 0 01-1 1A8 8 0 011 2a1 1 0 011-1z" fill="#666"/></svg>1.800.555.0142</span>
  <span><svg width="6" height="6" viewBox="0 0 10 10"><circle cx="5" cy="3" r="2.3" fill="#666"/><path d="M1 10a4 4 0 018 0z" fill="#666"/></svg>My Account</span>
  <span><svg width="6" height="6" viewBox="0 0 10 10"><path d="M5 9L1 5a2.3 2.3 0 014-3 2.3 2.3 0 014 3z" fill="#666"/></svg>My Wishlist</span>
  <span><svg width="6" height="6" viewBox="0 0 10 10"><rect x="2" y="4.5" width="6" height="5" fill="#666"/><path d="M3 4.5V3a2 2 0 014 0v1.5" stroke="#666" fill="none"/></svg>Login</span>
  <span><svg width="6" height="6" viewBox="0 0 10 10"><rect x="1" y="2" width="7" height="7" fill="none" stroke="#666"/><path d="M4 6l5-5" stroke="#666"/></svg>Register</span>
</div>

<div class="abs search"><svg width="6" height="6" viewBox="0 0 10 10"><circle cx="4" cy="4" r="3" stroke="#555" stroke-width="1.4" fill="none"/><path d="M6.3 6.3L9 9" stroke="#555" stroke-width="1.4"/></svg>SEARCH PRODUCTS</div>

<div class="abs cart">
  <svg width="14" height="13" viewBox="0 0 14 13"><path d="M0 1h2.5l2 7h7l1.5-5H4" stroke="#555" stroke-width="1.1" fill="none"/><circle cx="5.5" cy="11" r="1.2" fill="#555"/><circle cx="10.5" cy="11" r="1.2" fill="#555"/></svg>
  <span class="cart-badge">0</span>
  <div class="cart-text">MY CART<b>$0.00</b></div>
</div>

<nav class="abs main-nav">
  <a class="active" href="#">Home</a>
  <a href="#">Products</a>
  <a href="#">Our locations</a>
  <a href="#">Environmental protection</a>
  <a href="#">Science</a>
</nav>

<!-- hero -->
<section class="abs hero">
  <div class="hero-photo" role="img" aria-label="Looking up through tall moss-covered forest trees towards a bright canopy"></div>
</section>
<div class="abs hero-title">FRESH Air</div>
<div class="abs hero-sub">Bring awareness among people to say how polluted the planet is</div>
<svg class="abs" style="left:40px;top:181px" width="20" height="34" viewBox="0 0 20 34"><path d="M17 2L3 17l14 15" stroke="#d9d9d9" stroke-width="3" fill="none"/></svg>
<svg class="abs" style="left:656px;top:181px" width="20" height="34" viewBox="0 0 20 34"><path d="M3 2l14 15L3 32" stroke="#d9d9d9" stroke-width="3" fill="none"/></svg>
<div class="abs dots"><i class="on"></i><i></i><i></i><i></i></div>

<!-- welcome -->
<section class="abs welcome">
  <h1>WELCOME TO OUR SITE</h1>
  <p>There are many variations of passages of Lorem Ipsum available, but the majority have suffered alteration in some form, by injected humour, or randomised words which don't look even slightly believable. If you are going to use a passage of Lorem Ipsum. All the Lorem Ipsum generators on the Internet tend to repeat predefine Vivamus aliquet mi mi, a volutpat diam .</p>
  <span class="btn-green">READ MORE</span>
</section>

<!-- featured products -->
<div class="abs band"></div>
<div class="abs tabs"><span class="on">FEATURE PRODUCTS</span><span>NEW ARRIVALS</span><span>SPECIALS</span></div>
<div class="abs pager" style="top:447px">
  <svg width="7" height="10" viewBox="0 0 7 10"><path d="M6 1L2 5l4 4" stroke="#555" stroke-width="1.3" fill="none"/></svg>
  <svg width="7" height="10" viewBox="0 0 7 10"><path d="M1 1l4 4-4 4" stroke="#555" stroke-width="1.3" fill="none"/></svg>
</div>

<div class="abs grid" style="top:469px">
  <article class="card">
    <svg class="wish" width="10" height="9" viewBox="0 0 10 9"><path d="M5 8.3L1.2 4.5a2.2 2.2 0 013.8-3 2.2 2.2 0 013.8 3z" stroke="#999" fill="none"/></svg>
    <div class="shot white" role="img" aria-label="White aerosol can of bottled air"></div>
    <div class="name">Clearpeak 1</div><div class="price">$28.99</div>
    <div class="btn-cart"><svg width="6" height="5" viewBox="0 0 12 10"><path d="M0 1h2l2 6h6l2-5H3" stroke="#fff" stroke-width="1.6" fill="none"/></svg>ADD TO CART</div>
  </article>
  <article class="card">
    <svg class="wish" width="10" height="9" viewBox="0 0 10 9"><path d="M5 8.3L1.2 4.5a2.2 2.2 0 013.8-3 2.2 2.2 0 013.8 3z" stroke="#999" fill="none"/></svg>
    <div class="shot silver" role="img" aria-label="Silver-capped white roll-on bottle of air"></div>
    <div class="name">Clearpeak 2</div><div class="price">$19.99</div>
    <div class="btn-cart"><svg width="6" height="5" viewBox="0 0 12 10"><path d="M0 1h2l2 6h6l2-5H3" stroke="#fff" stroke-width="1.6" fill="none"/></svg>ADD TO CART</div>
  </article>
  <article class="card">
    <svg class="wish" width="10" height="9" viewBox="0 0 10 9"><path d="M5 8.3L1.2 4.5a2.2 2.2 0 013.8-3 2.2 2.2 0 013.8 3z" stroke="#999" fill="none"/></svg>
    <div class="shot red" role="img" aria-label="Red spray can of bottled air"></div>
    <div class="name">Clearpeak 3</div><div class="price">$48.99</div>
    <div class="btn-cart"><svg width="6" height="5" viewBox="0 0 12 10"><path d="M0 1h2l2 6h6l2-5H3" stroke="#fff" stroke-width="1.6" fill="none"/></svg>ADD TO CART</div>
  </article>
  <article class="card">
    <svg class="wish" width="10" height="9" viewBox="0 0 10 9"><path d="M5 8.3L1.2 4.5a2.2 2.2 0 013.8-3 2.2 2.2 0 013.8 3z" stroke="#999" fill="none"/></svg>
    <div class="shot blue" role="img" aria-label="Blue aluminium bottle of air"></div>
    <div class="name">Clearpeak 4</div><div class="price">$28.99</div>
    <div class="btn-cart"><svg width="6" height="5" viewBox="0 0 12 10"><path d="M0 1h2l2 6h6l2-5H3" stroke="#fff" stroke-width="1.6" fill="none"/></svg>ADD TO CART</div>
  </article>
</div>

<!-- best sellers -->
<div class="abs section-title" style="top:677px">BEST SELLERS</div>
<div class="abs pager" style="top:677px">
  <svg width="7" height="10" viewBox="0 0 7 10"><path d="M6 1L2 5l4 4" stroke="#555" stroke-width="1.3" fill="none"/></svg>
  <svg width="7" height="10" viewBox="0 0 7 10"><path d="M1 1l4 4-4 4" stroke="#555" stroke-width="1.3" fill="none"/></svg>
</div>

<div class="abs grid" style="top:699px">
  <article class="card">
    <svg class="wish" width="10" height="9" viewBox="0 0 10 9"><path d="M5 8.3L1.2 4.5a2.2 2.2 0 013.8-3 2.2 2.2 0 013.8 3z" stroke="#999" fill="none"/></svg>
    <div class="shot white" role="img" aria-label="White pump bottle of air"></div>
    <div class="name">Clearpeak 1</div><div class="price">$28.99</div>
    <div class="btn-cart"><svg width="6" height="5" viewBox="0 0 12 10"><path d="M0 1h2l2 6h6l2-5H3" stroke="#fff" stroke-width="1.6" fill="none"/></svg>ADD TO CART</div>
  </article>
  <article class="card">
    <svg class="wish" width="10" height="9" viewBox="0 0 10 9"><path d="M5 8.3L1.2 4.5a2.2 2.2 0 013.8-3 2.2 2.2 0 013.8 3z" stroke="#999" fill="none"/></svg>
    <div class="shot silver" role="img" aria-label="Silver-capped white roll-on bottle of air"></div>
    <div class="name">Clearpeak 2</div><div class="price">$28.99</div>
    <div class="btn-cart"><svg width="6" height="5" viewBox="0 0 12 10"><path d="M0 1h2l2 6h6l2-5H3" stroke="#fff" stroke-width="1.6" fill="none"/></svg>ADD TO CART</div>
  </article>
  <article class="card">
    <svg class="wish" width="10" height="9" viewBox="0 0 10 9"><path d="M5 8.3L1.2 4.5a2.2 2.2 0 013.8-3 2.2 2.2 0 013.8 3z" stroke="#999" fill="none"/></svg>
    <div class="shot white" role="img" aria-label="White capped canister of air"></div>
    <div class="name">Clearpeak 3</div><div class="price">$28.99</div>
    <div class="btn-cart"><svg width="6" height="5" viewBox="0 0 12 10"><path d="M0 1h2l2 6h6l2-5H3" stroke="#fff" stroke-width="1.6" fill="none"/></svg>ADD TO CART</div>
  </article>
  <article class="card">
    <svg class="wish" width="10" height="9" viewBox="0 0 10 9"><path d="M5 8.3L1.2 4.5a2.2 2.2 0 013.8-3 2.2 2.2 0 013.8 3z" stroke="#999" fill="none"/></svg>
    <div class="shot blue" role="img" aria-label="Blue aluminium bottle of air"></div>
    <div class="name">Clearpeak 4</div><div class="price">$28.99</div>
    <div class="btn-cart"><svg width="6" height="5" viewBox="0 0 12 10"><path d="M0 1h2l2 6h6l2-5H3" stroke="#fff" stroke-width="1.6" fill="none"/></svg>ADD TO CART</div>
  </article>
</div>

<!-- features -->
<div class="abs features">
  <div class="feature">
    <svg width="18" height="22" viewBox="0 0 18 22"><path d="M9 22V6M9 12l-5-4M9 9l5-4M9 15l4-3M4 8l-2-3M14 5l1-3M9 6V1" stroke="#fff" stroke-width="1.4" fill="none" stroke-linecap="round"/></svg>
    <h3>PURE AIR</h3>
    <p>There are many variations of passages of<br>Lorem Ipsum available</p>
  </div>
  <div class="feature">
    <svg width="20" height="22" viewBox="0 0 20 22"><path d="M3 14V10a7 7 0 0114 0v4" stroke="#fff" stroke-width="2" fill="none"/><rect x="2" y="12" width="4" height="7" rx="1.5" fill="#fff"/><rect x="14" y="12" width="4" height="7" rx="1.5" fill="#fff"/></svg>
    <h3>CUSTOMER SERVICE</h3>
    <p>There are many variations of passages of<br>Lorem Ipsum available</p>
  </div>
  <div class="feature">
    <svg width="26" height="22" viewBox="0 0 26 22"><path d="M2 4h13v11H2zM15 8h5l4 4v3h-9z" stroke="#fff" stroke-width="1.5" fill="none" stroke-linejoin="round"/><circle cx="7" cy="17" r="2.3" stroke="#fff" stroke-width="1.5" fill="var(--green)"/><circle cx="19" cy="17" r="2.3" stroke="#fff" stroke-width="1.5" fill="var(--green)"/></svg>
    <h3>FREE SHIPPING</h3>
    <p>There are many variations of passages of<br>Lorem Ipsum available</p>
  </div>
</div>

<!-- newsletter -->
<section class="abs newsletter">
  <h2>NEWSLETTER SIGNUP</h2>
  <div class="field" style="left:63px;width:147px"><svg width="6" height="6" viewBox="0 0 10 10"><circle cx="5" cy="3" r="2.3" fill="#888"/><path d="M1 10a4 4 0 018 0z" fill="#888"/></svg>Name</div>
  <div class="field" style="left:217px;width:148px"><svg width="7" height="5" viewBox="0 0 12 9"><rect width="12" height="9" fill="#888"/><path d="M0 0l6 5 6-5" stroke="#fff" fill="none"/></svg>E mail id</div>
  <div class="signup">SIGNUP!</div>
</section>

<!-- footer -->
<footer class="abs footer"></footer>
<div class="abs footer-brand"><span class="brand-mark"></span><span class="brand-name">Clearpeak Air</span></div>
<div class="abs copyright">Copyrights @ 2016 All Rights reserved</div>

<div class="abs fcol" style="left:220px">
  <h4>CONTACT US</h4>
  218 Larkfield Lane<br>Dayton, OH 45402<br>1.800.555.0142
</div>
<div class="abs fcol" style="left:334px">
  <h4>MENU</h4>
  Home<br>Products<br>Our locations<br>Environmental protection<br>Science.
</div>
<div class="abs fcol" style="left:451px">
  <h4>LINKS</h4>
  About Us<br>Contact Us<br>Customer Service<br>Privacy Policy<br>Orders and Returns<br>Shipping Information
</div>
<div class="abs fcol" style="left:564px">
  <h4>CONNECT WITH US</h4>
  <div class="social"><i></i>Feedbook</div>
  <div class="social"><i></i>Chirper</div>
  <div class="social"><i></i>Linkup</div>
  <div class="social"><i></i>RSS Feed</div>
</div>

</body>
</html>
```